Etikett für einen Rosé Wein
Zielgruppe
Wir sind ein Weingut und benötigen ein neues Etikett für unseren Muskattrollinger Rosé. Unsere Kunden sind eher traditionelle Weinkäufer.
Aufgabenstellung
Format:
Höhe: 9 cm
Breite: 11 cm
Da es nur ein Vorderetikett gibt, müssen alle relevanten Angaben (Hersteller, Alkohol, Inhalt in L, Rebsorte, etc.) enthalten sein. (siehe Flaschenabbildung anbei)
WÜRTTEMBERG
2019er
Muskattrollinger Rosé
DEUTSCHER QUALITÄTSWEIN
11,0 % Vol.
0,75 l
Enthält Sulfite
A.P.Nr. 58127364
Abfüller
Straße / PLZ / Ort / Tel.
Der Flaschenverschluss ist schwarz d.h. das neue Etikettendesign sollte dazu passen.
Bisher ist der Hintergrund des Weinetiketts schwarz. Dies muss jedoch nicht so bleiben.
Im Anhang finden Sie außerdem ein Plakat. Ggf. können Sie für das Flaschendesign einige nostalgische Elemente davon übernehmen.

```html
<!DOCTYPE html>
<html lang="de">
<head>
<meta charset="utf-8">
<title>Muskattrollinger Rosé – Etikett</title>
<link rel="stylesheet" href="https://fonts.googleapis.com/css2?family=Grenze+Gotisch:wght@500;600&family=Alegreya:wght@500;700&display=swap">
<style>
  :root {
    --page-bg: #ffffff;
    --label-bg: #333333;
    --ink: #ffffff;
    --ornament-tone: #4a4a4a;
    --illustration-tone: #5a5a5a;
  }
  html, body {
    margin: 0;
    padding: 0;
    width: 667px;
    height: 1200px;
    overflow: hidden;
    background: var(--page-bg);
  }
  .canvas {
    position: relative;
    width: 667px;
    height: 1200px;
  }
  .wine-label {
    position: absolute;
    left: 33px;
    top: 355px;
    width: 600px;
    height: 490px;
    display: block;
  }
  .label-ground { fill: var(--label-bg); }
  .frame-line { stroke: var(--ink); stroke-width: 1.6; fill: none; }
  .ornament-area { fill: var(--ornament-tone); }
  .grape-illustration { fill: var(--illustration-tone); }
  .gothic {
    font-family: "Grenze Gotisch", "UnifrakturMaguntia", serif;
    font-weight: 600;
    fill: var(--ink);
  }
  .serif {
    font-family: "Alegreya", Georgia, serif;
    font-weight: 700;
    fill: var(--ink);
  }
  .spec { font-size: 25px; }
  .quality-arc { font-size: 17px; letter-spacing: 0.5px; }
  .region { font-size: 22px; letter-spacing: 1px; }
  .wine-name { font-size: 62px; }
  .legal { font-size: 17px; font-weight: 500; }
  .bottler { font-size: 22px; font-weight: 500; }
</style>
</head>
<body>
<div class="canvas">
  <svg class="wine-label" viewBox="0 0 600 490" xmlns="http://www.w3.org/2000/svg">
    <defs>
      <path id="quality-curve" d="M 150 98 Q 301 -4 452 98"/>
    </defs>

    <rect class="label-ground" x="0" y="0" width="600" height="490"/>

    <!-- frame -->
    <polyline class="frame-line" points="144,19 23,19 23,470 144,470"/>
    <polyline class="frame-line" points="455,19 576,19 576,470 455,470"/>

    <!-- flourishes -->
    <rect class="ornament-area" x="158" y="10" width="284" height="28" rx="14" role="img" aria-label="Verschnörkelte Zierleiste oben"/>
    <rect class="ornament-area" x="158" y="452" width="284" height="28" rx="14" role="img" aria-label="Verschnörkelte Zierleiste unten"/>

    <!-- corner details -->
    <text class="gothic spec" x="35" y="60">11,0 % Vol.</text>
    <text class="gothic spec" x="35" y="87">0,75 l</text>
    <text class="gothic spec" x="563" y="60" text-anchor="end">2019er</text>

    <!-- quality designation -->
    <text class="serif quality-arc">
      <textPath href="#quality-curve" startOffset="50%" text-anchor="middle">DEUTSCHER QUALITÄTSWEIN</textPath>
    </text>

    <rect class="grape-illustration" x="232" y="90" width="143" height="52" rx="20" role="img" aria-label="Zeichnung einer Weintraube mit Rebblatt"/>

    <text class="serif region" x="301" y="175" text-anchor="middle">WÜRTTEMBERG</text>

    <!-- wine name -->
    <text class="gothic wine-name" x="301" y="267" text-anchor="middle">Muskattrollinger</text>
    <text class="gothic wine-name" x="301" y="316" text-anchor="middle">Rosé</text>

    <!-- legal info -->
    <text class="serif legal" x="35" y="366">Enthält Sulfite</text>
    <text class="serif legal" x="563" y="366" text-anchor="end">A.P. Nr.58127364</text>

    <!-- bottler -->
    <text class="serif bottler" x="301" y="410" text-anchor="middle">Abfüller</text>
    <text class="serif bottler" x="301" y="442" text-anchor="middle" xml:space="preserve">Straße  /  PLZ  /  Ort  /  Tel.</text>
  </svg>
</div>
</body>
</html>
```